【表紙要素】

■書籍タイトル
頼りない課長だった僕が十五期続いた欠損の倉庫業者を再生させた方法

■サブタイトル
町工場のための統率術入門

■キャッチコピー1
「灯台守ステップ術」で部下はあなたについてくる

■キャッチコピー2
特別セミナー動画(無料プレゼント)付き
「粗利が倍増する。倉庫業者が今日から使える5つの収益改善フレーム」

■著者
桐島のぶお

■肩書
物流マーケティングコンサルタント
次世代リーダー育成コンサルタント

■書籍の内容
総合物流会社から赤字続きの関連小会社へ出向となった著者が、会社を立て直す中で学んだリーダーシップ論がテーマになっています。原稿も添付いたします。

■ターゲット
運輸会社の経営者・部課長をターゲットとしています。

■デザイン要望
・イラストを入れるとすると、売上が右肩上がりになっているグラフなどのイメージかなと思いってます。もちろん、その他に良いアイデアがあれば採用したいと思います。
・イラストが入っても、文字だけでも、どちらでも構いません。できれば両方のパターンを比較して決めたいと思います。
・タイトルに関しては、「頼りない課長だった僕が」は小さく、「赤字」「黒字化」は目立つようにお願いします。

本の本文の内容が、あまり堅苦しくない、おもしろおかしい要素が含まれていますので、表紙も明るくてポップな感じが気に入りました。
ただし、誠に申し訳ないのですが、急遽、電子書籍のタイトルを変更することになりました。また、表紙の文字数も減らすことにしました。
したがいまして、今回のコンペとは別に、本日中に再発注をかけます。
何卒、ご理解いただき、再度コンペへのご参加をお願いいたします。

ご提案いただき、ありがとうございました。また、原稿を読んで頂き、内容を踏まえた上でデザインを考えていただき、大変感謝しています。
いろいろと考えた結果、急遽、電子書籍のタイトルを変更することになりました。今回のコンペとは別に、再度依頼をかけますので、またコンペにご参加いただけますようお願いいたします。

```html
<!DOCTYPE html>
<html lang="ja">
<head>
<meta charset="UTF-8">
<title>頼りない課長だった僕が十五期続いた欠損の倉庫業者を再生させた方法</title>
<link href="https://fonts.googleapis.com/css2?family=Noto+Sans+JP:wght@400;500;700;900&display=swap" rel="stylesheet">
<style>
  :root {
    --paper: #ffffff;
    --ink: #1f1f1f;
    --ink-soft: #4a4a4a;
    --accent-red: #e0261c;
    --accent-yellow: #f5d21a;
    --yellow-soft: #fff6c2;
    --figure-tone: #d9d2c4;
  }
  html, body {
    margin: 0;
    padding: 0;
    overflow: hidden;
    background: var(--paper);
  }
  .cover {
    position: relative;
    width: 843px;
    height: 1200px;
    background: var(--paper);
    overflow: hidden;
    font-family: "Noto Sans JP", sans-serif;
    color: var(--ink);
  }
  .vertical {
    position: absolute;
    writing-mode: vertical-rl;
    text-orientation: upright;
    white-space: nowrap;
    line-height: 1;
    transform: translateX(-50%);
  }
  .rising-graph {
    position: absolute;
    top: 0;
    left: 440px;
    width: 403px;
    height: 330px;
  }
  .leader-figure {
    position: absolute;
    top: 18px;
    left: 540px;
    width: 100px;
    height: 150px;
    border-radius: 40px 40px 10px 10px;
    background: linear-gradient(180deg, var(--figure-tone), #bfb6a5);
  }
  .subtitle-bubble {
    position: absolute;
    top: 120px;
    left: 330px;
    width: 225px;
    height: 92px;
  }
  .subtitle-bubble svg { position: absolute; inset: 0; }
  .subtitle-bubble p {
    position: relative;
    margin: 0;
    padding-top: 18px;
    text-align: center;
    font-size: 22px;
    font-weight: 700;
    line-height: 1.35;
  }
  .catch-method { left: 795px; top: 40px; font-size: 31px; font-weight: 700; }
  .title-lead { left: 675px; top: 300px; font-size: 38px; font-weight: 700; }
  .title-line { font-weight: 900; font-size: 82px; }
  .title-line .big { font-size: 120px; }
  .title-line .red { color: var(--accent-red); }
  .line-term { left: 575px; top: 460px; }
  .line-loss { left: 445px; top: 330px; }
  .line-revive { left: 295px; top: 400px; }
  .bonus-note { left: 36px; top: 30px; font-size: 26px; font-weight: 700; }
  .bonus-title { left: 108px; top: 360px; font-size: 23.5px; font-weight: 500; color: var(--ink-soft); }
  .author-card {
    position: absolute;
    left: 640px;
    top: 860px;
    width: 192px;
    padding: 18px 0 20px;
    background: var(--yellow-soft);
    border-top: 6px solid var(--accent-yellow);
    text-align: center;
  }
  .author-name { margin: 0 0 12px; font-size: 36px; font-weight: 900; letter-spacing: 0.04em; }
  .author-role { margin: 0; font-size: 11.5px; font-weight: 700; line-height: 1.6; }
</style>
</head>
<body>
<div class="cover">
  <svg class="rising-graph" viewBox="0 0 403 330" aria-hidden="true">
    <polygon points="0,330 250,110 236,96 330,40 300,140 286,126 40,330" fill="var(--accent-yellow)"/>
  </svg>
  <div class="leader-figure" role="img" aria-label="Illustration of a cheering business leader standing on the rising arrow"></div>

  <div class="subtitle-bubble">
    <svg viewBox="0 0 225 92" aria-hidden="true">
      <path d="M14 2 H211 Q223 2 223 14 V70 Q223 80 211 80 H150 L170 92 L128 80 H14 Q2 80 2 70 V14 Q2 2 14 2 Z" fill="var(--paper)" stroke="var(--ink)" stroke-width="2"/>
    </svg>
    <p>町工場のための<br>統率術入門</p>
  </div>

  <p class="vertical catch-method">「灯台守ステップ術」で部下はあなたについてくる</p>

  <h1 style="margin:0">
    <span class="vertical title-lead">頼りない課長だった僕が</span>
    <span class="vertical title-line line-term">十五期続いた</span>
    <span class="vertical title-line line-loss"><span class="big red">欠損</span>の倉庫業者を</span>
    <span class="vertical title-line line-revive"><span class="big">再生</span>させた方法</span>
  </h1>

  <p class="vertical bonus-note">特別セミナー動画（無料プレゼント）付き</p>
  <p class="vertical bonus-title">「粗利が倍増する。倉庫業者が今日から使える5つの収益改善フレーム」</p>

  <div class="author-card">
    <p class="author-name">桐島のぶお</p>
    <p class="author-role">物流マーケティングコンサルタント<br>次世代リーダー育成コンサルタント</p>
  </div>
</div>
</body>
</html>
```